QBoost480 Business Card Design

I am in need of a business card design.

Business Name: Quantum Boost 480 or Qboost480 (we can try the business card with both variations)

I would like it to be somewhat different from the "average" business card

What do we do?

We link up with distributors of different items and we Market their products, sell their products, fulfill the shipment, and handle all customer service that goes along with it.

I will be uploading our logo as well as other business card ideas that i have seen and liked on the web.

I like the style of the "graphic design" business card that i uploaded. I was thinking maybe something like that but instead would read.

SYNC | SELL | SHIP

With maybe:
a computer or a Sync icon underneath SYNC
Some form of money sign underneath Sell
a delivery truck or something underneath SHIP.

And then I was thinking maybe put the logo on the back side like in the other business card that i uploaded.

I definitely want a double sided business card.

These are only my suggestions and if i was very confident in my idea then I wouldn't have to be on here. (So make what you think is nice because my opinion is probably not so great anyway!!)

Everything can be changed.

ALSO, For the logo
We can try and remove the text multi channel selling

For the Business card contact info:
Milo Quenton
CEO
2914 Ravensby Street
J7T-2K8
Montreal, Quebec

Thanks

Target Market(s)

Businesses

Industry/Entity Type

Information Technology

Font styles to use
Serif
Sans Serif
Decorative

Colors
34a6d6
33b8a4
aaaaaa
85cae6
33a6d7
0492cd
9d9d9d

Requirements
Must have
• Double Sided Business card
Nice to have
• Illustration graphics / Icons underneath the main points

```html
<!DOCTYPE html>
<html lang="en">
<head>
<meta charset="utf-8">
<title>QBoost480 Business Card</title>
<link rel="stylesheet" href="https://fonts.googleapis.com/css2?family=Open+Sans:wght@400;600;700&display=swap">
<style>
  :root {
    --backdrop: #2f2a27;
    --card: #0c0c0c;
    --accent: #34a6d6;
    --wordmark: #e6e6e6;
    --text-light: #e6e6e6;
    --divider: #2a2a2a;
  }
  * { box-sizing: border-box; margin: 0; padding: 0; }
  html, body {
    width: 1200px;
    height: 900px;
    overflow: hidden;
    background: var(--backdrop);
    font-family: "Open Sans", Arial, sans-serif;
  }
  .stage {
    position: relative;
    width: 1200px;
    height: 900px;
  }
  .card {
    position: absolute;
    top: 295px;
    width: 540px;
    height: 310px;
    background: var(--card);
    box-shadow: 0 10px 30px rgba(0,0,0,0.45);
  }
  .card--front { left: 40px; }
  .card--back { left: 620px; }

  .brand-name {
    font-weight: 600;
    line-height: 1;
    color: var(--wordmark);
    white-space: nowrap;
  }

  /* front */
  .front-brand {
    position: absolute;
    left: 0;
    top: 0;
    width: 262px;
    height: 310px;
    display: flex;
    align-items: center;
    justify-content: center;
    padding-top: 60px;
  }
  .front-brand .brand-name { font-size: 34px; }
  .front-divider {
    position: absolute;
    left: 262px;
    top: 40px;
    width: 1px;
    height: 230px;
    background: var(--divider);
  }
  .contact {
    position: absolute;
    left: 290px;
    top: 58px;
    color: var(--text-light);
    font-size: 13px;
    line-height: 1.35;
  }
  .contact__name {
    color: var(--accent);
    font-weight: 700;
    font-size: 16px;
  }
  .contact__title { margin-bottom: 14px; }
  .contact__address { margin-bottom: 14px; }
  .contact__list { list-style: none; }
  .contact__list li {
    display: flex;
    align-items: center;
    gap: 8px;
  }
  .contact__icon {
    width: 11px;
    height: 11px;
    flex: none;
  }

  /* back */
  .card--back {
    display: flex;
    align-items: center;
    justify-content: center;
  }
  .card--back .brand-name { font-size: 60px; }
</style>
</head>
<body>
<main class="stage">
  <section class="card card--front" aria-label="Business card front">
    <div class="front-brand">
      <span class="brand-name">Qboost480</span>
    </div>
    <div class="front-divider"></div>
    <div class="contact">
      <p class="contact__name">Milo Quenton</p>
      <p class="contact__title">CEO</p>
      <p class="contact__address">2914 Ravensby Street<br>J7T-2K8 Montreal, Quebec</p>
      <ul class="contact__list">
        <li>
          <svg class="contact__icon" viewBox="0 0 12 12" aria-hidden="true">
            <path d="M1 3c0-1 1-2 2-2l1 2-1 1c.5 1.5 2.5 3.5 4 4l1-1 2 1c0 1-1 2-2 2C4 10 1 7 1 3z" fill="#34a6d6"/>
          </svg>
          <span>044-987 654 321</span>
        </li>
        <li>
          <svg class="contact__icon" viewBox="0 0 12 12" aria-hidden="true">
            <rect x="1" y="2.5" width="10" height="7" fill="#34a6d6"/>
            <path d="M1 2.5l5 4 5-4" fill="none" stroke="#0c0c0c" stroke-width="1"/>
          </svg>
          <span>info@qboost480.com</span>
        </li>
        <li>
          <svg class="contact__icon" viewBox="0 0 12 12" aria-hidden="true">
            <path d="M5 7l2-2M4 5.5L2.5 7a1.8 1.8 0 0 0 2.5 2.5L6.5 8M8 6.5L9.5 5A1.8 1.8 0 0 0 7 2.5L5.5 4" fill="none" stroke="#34a6d6" stroke-width="1.4" stroke-linecap="round"/>
          </svg>
          <span>www.qboost480.com</span>
        </li>
      </ul>
    </div>
  </section>

  <section class="card card--back" aria-label="Business card back">
    <span class="brand-name">Qboost480</span>
  </section>
</main>
</body>
</html>
```